Towing company card on one side and our Autobody and collision repair shop card on the other

We need a two sided business card on one side it would be for our towing company and the other for our auto body and collision repair shop we would like our logo to appear on the card on the autobody shop side .I would like the card to be unique not just a regular towing or auto body shop company card. Our tow truck company offers flatbed and wheel lift service short and long distance we also offer roadside assistance which covers jumpstarts, tire changes, lock outs we are on call 24/7. All of our trucks are state of the art and brand new with air ride suspension and low profile beds. The phone number for the towing company is 201-574-3902. We accept all major credit cards. The other side of the card would be for the Auto body shop specializing in auto painting, body and fender repair, frame straightening , unibody repair and fiberglass repair work. We color match factory paint and we handle all insurance companies claims.The phone number for the auto body shop is 201-368-2915 fax 201-368-2915 email redfinchautobody@mailvale.net the autobody license number must appear on the autobody side of the card in this format. LIC#04817C

Target Market(s)

new customers

Industry/Entity Type

Business

Contact Information for Business Card

towing company on one side and auto body and collision repair on the other side

Colors
ec1f27
000000
aaaaaa
e9e9e9
0555a3
959595
1b1b1b

Requirements
Must have
• Must have company logo on card on the autobody side of card and show address 4816 Garvick ave Eastwood NJ 07391

```html
<!DOCTYPE html>
<html lang="en">
<head>
<meta charset="utf-8">
<title>Red Finch Auto Body &amp; Towing – Business Card</title>
<link href="https://fonts.googleapis.com/css2?family=Exo+2:wght@500&family=Lato:wght@400;700&display=swap" rel="stylesheet">
<style>
  :root {
    --backdrop: #6b6b6b;
    --card-light: #f2f2f2;
    --brand-red: #c42a25;
    --ink: #1b1b1b;
    --white: #ffffff;
    --rule-light: #bdbdbd;
    --rule-dark: #e9a9a6;
  }
  * { margin: 0; padding: 0; box-sizing: border-box; }
  html, body { width: 1200px; height: 900px; overflow: hidden; }
  body {
    background: var(--backdrop);
    font-family: "Lato", Arial, sans-serif;
    position: relative;
  }
  .card {
    position: absolute;
    top: 170px;
    width: 347px;
    height: 561px;
    text-align: center;
  }
  .card--bodyshop { left: 259px; background: var(--card-light); color: var(--ink); }
  .card--towing { left: 631px; background: var(--brand-red); color: var(--white); }

  .brand {
    position: absolute;
    left: 0; right: 0;
    display: flex;
    align-items: center;
    justify-content: center;
    gap: 10px;
  }
  .card--bodyshop .brand { top: 110px; color: var(--brand-red); }
  .card--towing .brand { top: 122px; color: var(--white); }
  .brand__mark { width: 18px; height: 18px; border-radius: 50%; background: currentColor; flex: none; }
  .brand__name {
    font-family: "Lato", Arial, sans-serif;
    font-weight: 700;
    font-size: 22px;
    line-height: 1.15;
    text-transform: uppercase;
    letter-spacing: 0.5px;
  }

  .tagline {
    position: absolute;
    top: 192px; left: 0; right: 0;
    font-family: "Exo 2", Arial, sans-serif;
    font-weight: 500;
    font-size: 14.5px;
    letter-spacing: 0.4px;
    line-height: 18px;
    color: var(--brand-red);
    text-transform: uppercase;
  }
  .license { position: absolute; top: 251px; left: 0; right: 0; font-size: 16.5px; }
  .license__prefix { color: var(--brand-red); }

  .contact-icons {
    position: absolute;
    top: 314px; left: 87px; width: 173px;
    display: flex; align-items: center; gap: 6px;
  }
  .contact-icons .rule { flex: 1; height: 1px; background: var(--rule-light); }
  .contact-icons svg { width: 15px; height: 13px; fill: var(--brand-red); }

  .contact-list {
    position: absolute;
    top: 335px; left: 0; right: 0;
    font-size: 17.5px;
    line-height: 22px;
    list-style: none;
  }
  .divider { position: absolute; height: 1px; }
  .card--bodyshop .divider { top: 428px; left: 87px; width: 180px; background: var(--rule-light); }
  .card--towing .divider { top: 436px; left: 64px; width: 219px; background: var(--rule-dark); }

  .services {
    position: absolute;
    top: 455px; left: 0; right: 0;
    font-size: 15px;
    line-height: 18px;
  }
  .services .sep { color: var(--brand-red); padding: 0 5px; }

  .address {
    position: absolute;
    top: 518px; left: 0; right: 0;
    display: flex; align-items: center; justify-content: center; gap: 6px;
    font-size: 13.5px;
    line-height: 18px;
  }
  .address svg { width: 10px; height: 14px; fill: var(--brand-red); flex: none; }

  .towing-info {
    position: absolute;
    top: 259px; left: 10px; right: 10px;
    font-size: 15px;
    line-height: 19px;
  }
  .towing-info p { margin-bottom: 8px; }
  .on-call {
    position: absolute;
    top: 458px; left: 0; right: 0;
    font-size: 21px; font-weight: 700; letter-spacing: 0.3px;
  }
  .on-call-phone {
    position: absolute;
    top: 490px; left: 0; right: 0;
    font-size: 18.5px;
  }
</style>
</head>
<body>

<section class="card card--bodyshop" aria-label="Auto body shop side">
  <div class="brand">
    <span class="brand__mark" aria-hidden="true"></span>
    <span class="brand__name">Red Finch<br>Auto Body &amp; Towing</span>
  </div>
  <p class="tagline">We color match factory paint and we<br>handle all insurance companies claims</p>
  <p class="license"><span class="license__prefix">LIC</span>#04817C</p>

  <div class="contact-icons" aria-hidden="true">
    <span class="rule"></span>
    <svg viewBox="0 0 16 14"><path d="M2 5c0-2 3-3 6-3s6 1 6 3v1h-3V5H5v1H2zM4 7h8l2 6H2z"/></svg>
    <svg viewBox="0 0 16 14"><path d="M4 1h8v3H4zM1 5h14v6h-3v2H4v-2H1zM5 9v3h6V9z"/></svg>
    <svg viewBox="0 0 16 14"><path d="M1 2h14v10H1zM2 3l6 5 6-5v-.5H2z" fill-rule="evenodd"/></svg>
    <span class="rule"></span>
  </div>

  <ul class="contact-list">
    <li>201-368-2915</li>
    <li>201-368-2915</li>
    <li>redfinchautobody@mailvale.net</li>
  </ul>
  <div class="divider"></div>
  <p class="services">
    Auto painting<span class="sep">|</span>Body and fender repair<br>
    Frame straightening<span class="sep">|</span>Unibody repair and<br>
    fiberglass repair work
  </p>
  <p class="address">
    <svg viewBox="0 0 10 14" aria-hidden="true"><path d="M5 0a5 5 0 0 1 5 5c0 3.5-5 9-5 9S0 8.5 0 5a5 5 0 0 1 5-5zm0 3a2 2 0 1 0 0 4 2 2 0 0 0 0-4z" fill-rule="evenodd"/></svg>
    4816 Garvick ave Eastwood NJ 07391
  </p>
</section>

<section class="card card--towing" aria-label="Towing side">
  <div class="brand">
    <span class="brand__mark" aria-hidden="true"></span>
    <span class="brand__name">Red Finch<br>Auto Body &amp; Towing</span>
  </div>
  <div class="towing-info">
    <p>Flatbed and wheel lift service short and<br>long distance.</p>
    <p>we also offer roadside assistance which covers<br>jumpstarts, tire change outs and lock outs.</p>
    <p>Our trucks are state of the art and brand new<br>with air ride suspension and low profile beds.</p>
    <p>We accept all major credit cards.</p>
  </div>
  <div class="divider"></div>
  <p class="on-call">WE ARE ON CALL 24/7</p>
  <p class="on-call-phone">Phone- 201-574-3902</p>
</section>

</body>
</html>
```